I need a business Card Design for my practice , i am clinical herbalist. I am a herbalist specializing in Lyme disease, autism, autoimmune diseases, difficult to cure diseasesDifficult to cure diseases. In my innovative practice i link traditional medicine, herbs with science, immunologu ,pharmacology.

Industry/Entity Type

Business

Contact Information for Business Card

My company name : OŚRODEK ZIELNIK
My name : Piotr Kaleta
Name of my profession : Fitoterapeuta
In Polish language Fitoterapeuta is Herbalist .

e-mail: piotrkaleta@osrodekzielnik.com
www.osrodek-zielnik.pl
phone : 604 587 231
My company adress : Dąbrowa Sitnicka 41 , 38-415 Jodłowiec
I dont have logo .

Requirements
Nice to have
• My company

```html
<!DOCTYPE html>
<html lang="pl">
<head>
<meta charset="utf-8">
<title>Ośrodek Zielnik – wizytówka</title>
<link rel="stylesheet" href="https://fonts.googleapis.com/css2?family=Oswald:wght@700&family=Open+Sans:wght@400;600&display=swap">
<style>
  :root {
    --backdrop: #e9ece8;
    --card: #ffffff;
    --band: #1fe61f;
    --band-fold: #10c410;
    --band-icon: #17cf17;
    --title: #1b7a1b;
    --ink: #111511;
    --name: #ffffff;
    --art-light: #5fe05f;
    --art-dark: #138a13;
  }
  html, body {
    margin: 0;
    width: 1200px;
    height: 1016px;
    overflow: hidden;
    background: var(--backdrop);
  }
  .business-card {
    position: absolute;
    left: 150px;
    top: 255px;
    width: 900px;
    height: 506px;
    background: var(--card);
    box-shadow: 0 6px 24px rgba(0,0,0,0.12);
  }
  .business-card svg { display: block; width: 100%; height: 100%; }
  .company-name { font-family: "Oswald", "Arial Narrow", sans-serif; font-weight: 700; font-size: 34px; fill: var(--title); letter-spacing: 0.5px; }
  .person-name { font-family: "Open Sans", Arial, sans-serif; font-weight: 600; font-size: 30px; fill: var(--name); }
  .profession { font-family: "Open Sans", Arial, sans-serif; font-weight: 400; font-size: 19px; fill: var(--ink); }
  .contact-text { font-family: "Open Sans", Arial, sans-serif; font-weight: 400; fill: var(--ink); }
  .band { fill: var(--band); }
  .band-fold { fill: var(--band-fold); }
  .band-icon { fill: none; stroke: var(--band-icon); stroke-width: 2; stroke-linejoin: round; }
</style>
</head>
<body>
<div class="business-card">
  <svg viewBox="0 0 680 382" xmlns="http://www.w3.org/2000/svg">
    <defs>
      <linearGradient id="herb-art" x1="0" y1="0" x2="1" y2="1">
        <stop offset="0" stop-color="var(--art-light)"/>
        <stop offset="1" stop-color="var(--art-dark)"/>
      </linearGradient>
    </defs>

    <rect x="42" y="25" width="158" height="155" fill="url(#herb-art)" role="img" aria-label="Zielony krzyż apteczny z lawendą i stokrotkami"/>
    <rect x="212" y="92" width="36" height="62" rx="10" fill="url(#herb-art)" role="img" aria-label="Listek ziela nad kapsułką"/>

    <text class="company-name" x="252" y="101">OŚRODEK ZIELNIK</text>

    <!-- name band -->
    <polygon class="band-fold" points="628,137 688,165 688,203 628,173"/>
    <rect class="band" x="238" y="137" width="390" height="36"/>
    <text x="252" y="166"><tspan class="person-name">Piotr Kaleta</tspan><tspan class="profession" dx="8">FITOTERAPEUTA</tspan></text>

    <!-- address band -->
    <polygon class="band-fold" points="628,182 688,212 688,280 628,250"/>
    <rect class="band" x="358" y="182" width="270" height="68"/>
    <g class="band-icon">
      <rect x="372" y="196" width="20" height="26" rx="2"/>
      <path d="M377 204h10M377 210h10M377 216h6"/>
    </g>
    <text class="contact-text" font-size="20" x="404" y="210">Dąbrowa Sitnicka 41</text>
    <text class="contact-text" font-size="20" x="404" y="239">38-415 Jodłowiec</text>

    <!-- phone band -->
    <polygon class="band-fold" points="8,225 68,200 68,240 8,265"/>
    <rect class="band" x="68" y="200" width="240" height="40"/>
    <g class="band-icon">
      <rect x="81" y="207" width="14" height="25" rx="3"/>
      <path d="M85 227h6"/>
    </g>
    <text class="contact-text" font-size="24" x="112" y="230">604 587 231</text>

    <!-- web band -->
    <polygon class="band-fold" points="8,282 68,255 68,292 8,320"/>
    <rect class="band" x="68" y="255" width="272" height="37"/>
    <path class="band-icon" d="M78 274l10-10 10 10M81 272v14h14v-14"/>
    <text class="contact-text" font-size="17" x="112" y="280">www.osrodek-zielnik.pl</text>

    <!-- email band -->
    <polygon class="band-fold" points="615,308 680,342 680,378 615,345"/>
    <rect class="band" x="195" y="308" width="420" height="37"/>
    <g class="band-icon">
      <rect x="208" y="318" width="24" height="16"/>
      <path d="M208 318l12 9 12-9"/>
    </g>
    <text class="contact-text" font-size="18" x="250" y="333">piotrkaleta@osrodekzielnik.com</text>
  </svg>
</div>
</body>
</html>
```